Thornwell Building Company - advertisement poster

I am looking to print some canvas signs to advertise my general contracting company, Thornwell Building Company. The sign will measure 6' long x 3' high so the size should match that ratio. I already have a logo icon, which is the Letter 'A' and some trees that I would like to incorporate, see attached. I would also like the to have the following information listed:
1) phone number: 472-318-6095
2) email: thornwellbuildingcompany@mailvistra.net
3) website: thornwellbuildingcompany.com
4) Lic#5386204
5) I want to use this text: "BUILD WITH THE T-CREW!"

The ad should be relatively simple and clean. Black and Green are my company colors. I am open to creative ideas!

Target Market(s)

People looking to renovate their homes

Industry/Entity Type

Construction

Colors
59FF00
82FF00
B8FF75
E3FFCB
F4FFEA

Requirements
Must have
• Must have my company logo
Should not have
• No photos or complex graphics

```html
<!DOCTYPE html>
<html lang="en">
<head>
<meta charset="utf-8">
<title>Thornwell Building Company – Sign</title>
<link rel="stylesheet" href="https://fonts.googleapis.com/css2?family=Archivo+Black&family=Montserrat:wght@500;600;700&display=swap">
<style>
  :root {
    --stage: #e9ece6;
    --brand-green: #6db33f;
    --ink: #1b1b1b;
    --white: #ffffff;
  }
  * { box-sizing: border-box; margin: 0; padding: 0; }
  html, body {
    width: 1200px;
    height: 800px;
    overflow: hidden;
    background: var(--stage);
  }
  .sign {
    position: absolute;
    left: 50px;
    top: 125px;
    width: 1100px;
    height: 550px;
    background: var(--brand-green);
    font-family: "Montserrat", sans-serif;
    color: var(--ink);
  }
  .brand-block {
    position: absolute;
    left: 64px;
    top: 0;
    width: 300px;
    height: 225px;
    background: var(--ink);
    display: flex;
    flex-direction: column;
    align-items: center;
    justify-content: center;
    gap: 14px;
  }
  .brand-mark {
    width: 46px;
    height: 46px;
    background: var(--brand-green);
  }
  .brand-name {
    font-family: "Montserrat", sans-serif;
    font-weight: 700;
    color: var(--white);
    text-align: center;
    font-size: 24px;
    line-height: 1.2;
    letter-spacing: 1px;
  }
  .licence {
    position: absolute;
    right: 76px;
    top: 178px;
    font-size: 11px;
    font-weight: 500;
  }
  .headline {
    position: absolute;
    left: 0;
    right: 0;
    top: 268px;
    text-align: center;
    font-family: "Archivo Black", sans-serif;
    font-size: 72px;
    line-height: 1;
    letter-spacing: 0.5px;
  }
  .contact-row {
    position: absolute;
    left: 0;
    right: 0;
    top: 388px;
    display: flex;
    justify-content: center;
    align-items: center;
    gap: 30px;
  }
  .email {
    display: flex;
    align-items: center;
    gap: 12px;
    font-size: 19px;
    font-weight: 500;
    letter-spacing: 0.6px;
  }
  .email svg { width: 22px; height: 16px; }
  .phone {
    background: var(--ink);
    color: var(--brand-green);
    font-weight: 700;
    font-size: 38px;
    padding: 4px 16px 4px 40px;
    letter-spacing: 0.5px;
  }
  .website {
    position: absolute;
    left: 0;
    right: 0;
    top: 472px;
    display: flex;
    justify-content: center;
    align-items: center;
    gap: 20px;
    font-size: 40px;
    font-weight: 500;
  }
  .website svg { width: 42px; height: 42px; }
</style>
</head>
<body>
  <section class="sign">
    <div class="brand-block">
      <div class="brand-mark"></div>
      <div class="brand-name">THORNWELL<br>BUILDING COMPANY</div>
    </div>

    <p class="licence">Licence No. 5386204</p>

    <h1 class="headline">Build with the T-Crew!</h1>

    <div class="contact-row">
      <div class="email">
        <svg viewBox="0 0 22 16" aria-hidden="true">
          <rect x="1" y="1" width="20" height="14" fill="var(--ink)"/>
          <polyline points="1,1 11,9 21,1" fill="none" stroke="var(--brand-green)" stroke-width="1.6"/>
        </svg>
        <span>ThornwellBuildingCompany@mailvistra.net</span>
      </div>
      <div class="phone">472.318.6095</div>
    </div>

    <div class="website">
      <svg viewBox="0 0 42 42" aria-hidden="true" fill="none" stroke="var(--ink)" stroke-width="2.6">
        <circle cx="21" cy="21" r="18"/>
        <ellipse cx="21" cy="21" rx="8" ry="18"/>
        <line x1="3" y1="21" x2="39" y2="21"/>
        <line x1="6" y1="12" x2="36" y2="12"/>
        <line x1="6" y1="30" x2="36" y2="30"/>
      </svg>
      <span>ThornwellBuildingCompany.com</span>
    </div>
  </section>
</body>
</html>
```